Harbor Hide Revival Product Label

We need a design for a label to be used on bottles of leather cleaner and conditioner products that will be used in curated kits. We would like it to incorporate our business logo as well as have an area that we can fill in later with the appropriate product name as needed. We would like to see designs that use shades of brown, but we are open to other colors often seen in leather. I am including the Harbor Hide business Logo below, however again we would prefer to have the label in various shades of browns, rather than the red and grey, more like the mock-up that I am also attaching.

*** I am attaching examples of the types of bottles that will be used. They vary in size from 8 oz to 16 oz. if you are designing a label for a spray bottle they are from 16-32 oz. ***

```html
<!DOCTYPE html>
<html lang="en">
<head>
<meta charset="utf-8">
<title>Harbor Hide Revival – Leather Cleaner &amp; Conditioner Labels</title>
<link rel="stylesheet" href="https://fonts.googleapis.com/css2?family=Montserrat:ital,wght@0,600;0,800;0,900;1,900&family=Open+Sans:wght@400&family=Poppins:wght@600&display=swap">
<style>
  :root {
    --board: #3b3b3d;
    --maroon: #7b1a22;
    --maroon-deep: #4a0e13;
    --maroon-bright: #8e1d26;
    --charcoal: #3e3e40;
    --paper: #ffffff;
    --halftone: #e6e6e6;
    --gold-dark: #8a6a2a;
    --gold-light: #efd998;
  }
  html, body {
    margin: 0;
    width: 1035px;
    height: 1200px;
    overflow: hidden;
    background: var(--board);
  }
  .board {
    position: relative;
    width: 1035px;
    height: 1200px;
  }
  .option-title {
    position: absolute;
    top: 50px;
    width: 347px;
    margin: 0;
    text-align: center;
    font-family: "Open Sans", sans-serif;
    font-weight: 400;
    font-size: 44px;
    color: var(--paper);
    letter-spacing: 0.5px;
  }
  .label {
    position: absolute;
    top: 138px;
    width: 347px;
    height: 949px;
    box-shadow: 10px 12px 18px rgba(0,0,0,0.45);
  }
  .label svg { display: block; width: 100%; height: 100%; }
  .option-one { left: 124px; }
  .option-two { left: 564px; }
  .brand-name { font-family: "Montserrat", sans-serif; font-weight: 600; fill: var(--maroon); }
  .product-word { font-family: "Poppins", sans-serif; font-weight: 600; }
  .product-line { font-family: "Montserrat", sans-serif; font-weight: 900; fill: var(--paper); }
  .net-weight { font-family: "Montserrat", sans-serif; font-weight: 900; }
</style>
</head>
<body>
<main class="board">
  <h2 class="option-title" style="left:124px">option-01</h2>
  <h2 class="option-title" style="left:564px">option-02</h2>

  <!-- Label option one -->
  <section class="label option-one">
    <svg viewBox="0 0 502 1375" xmlns="http://www.w3.org/2000/svg">
      <defs>
        <linearGradient id="gold-a" x1="0" y1="1" x2="0" y2="0">
          <stop offset="0" stop-color="var(--gold-dark)"/>
          <stop offset="0.55" stop-color="var(--gold-light)"/>
          <stop offset="1" stop-color="#b8924a"/>
        </linearGradient>
        <linearGradient id="paper-fade-a" x1="0" y1="0" x2="1" y2="1">
          <stop offset="0" stop-color="var(--halftone)"/>
          <stop offset="0.35" stop-color="var(--paper)"/>
        </linearGradient>
        <linearGradient id="seat-brown" x1="0" y1="0" x2="1" y2="1">
          <stop offset="0" stop-color="#a0674a"/>
          <stop offset="0.5" stop-color="#7a4630"/>
          <stop offset="1" stop-color="#3a2a24"/>
        </linearGradient>
        <linearGradient id="maroon-a" x1="0" y1="0" x2="1" y2="1">
          <stop offset="0" stop-color="var(--maroon-deep)"/>
          <stop offset="1" stop-color="var(--maroon)"/>
        </linearGradient>
        <clipPath id="label-a-clip"><rect width="502" height="1375"/></clipPath>
      </defs>
      <g clip-path="url(#label-a-clip)">
        <rect class="label-paper" width="502" height="1375" fill="url(#paper-fade-a)"/>
        <rect y="1230" width="502" height="145" fill="var(--paper)"/>

        <path class="brand-rule" d="M0,700 C0,470 150,360 300,300 L502,160" fill="none" stroke="var(--charcoal)" stroke-width="16"/>

        <path class="maroon-band" d="M0,630 C40,800 180,880 330,870 C420,862 470,830 502,800 L502,1080 C380,1180 200,1212 0,1215 Z" fill="url(#maroon-a)"/>
        <path d="M250,875 C360,885 450,845 502,805" fill="none" stroke="var(--charcoal)" stroke-width="14"/>
        <path d="M0,1226 C200,1224 400,1172 502,1094" fill="none" stroke="var(--charcoal)" stroke-width="12"/>

        <circle cx="290" cy="595" r="258" fill="var(--paper)"/>
        <circle cx="295" cy="595" r="245" fill="url(#seat-brown)" role="img" aria-label="Photo of tan leather car seats with lumbar pillows"/>

        <g class="brand-lockup" transform="translate(80,340) rotate(-22)">
          <circle cx="40" cy="-30" r="40" fill="var(--maroon)"/>
          <text class="brand-name" x="95" y="-22" font-size="40">HARBOR HIDE</text>
          <text class="brand-name" x="97" y="0" font-size="16" letter-spacing="1">REVIVAL, INC</text>
        </g>

        <g class="product-title" transform="rotate(-12 250 1060)">
          <text class="product-word" x="45" y="1060" font-size="128" textLength="395" lengthAdjust="spacingAndGlyphs" fill="url(#gold-a)">Leather</text>
          <text class="product-line" x="138" y="1102" font-size="44" textLength="245" lengthAdjust="spacingAndGlyphs">CLEANER &amp;</text>
          <text class="product-line" x="112" y="1148" font-size="44" textLength="320" lengthAdjust="spacingAndGlyphs">CONDITIONER</text>
        </g>

        <text class="net-weight" x="251" y="1305" font-size="34" text-anchor="middle" fill="var(--maroon)">16 oz</text>
      </g>
    </svg>
  </section>

  <!-- Label option two -->
  <section class="label option-two">
    <svg viewBox="0 0 502 1375" xmlns="http://www.w3.org/2000/svg">
      <defs>
        <linearGradient id="gold-b" x1="0" y1="1" x2="0" y2="0">
          <stop offset="0" stop-color="var(--gold-dark)"/>
          <stop offset="0.55" stop-color="var(--gold-light)"/>
          <stop offset="1" stop-color="#b8924a"/>
        </linearGradient>
        <linearGradient id="seat-black" x1="0" y1="0" x2="1" y2="1">
          <stop offset="0" stop-color="#3a3536"/>
          <stop offset="0.5" stop-color="#141213"/>
          <stop offset="1" stop-color="#2a1416"/>
        </linearGradient>
        <linearGradient id="maroon-b" x1="0" y1="0" x2="0.3" y2="1">
          <stop offset="0" stop-color="var(--maroon-deep)"/>
          <stop offset="0.6" stop-color="#3a0b0f"/>
          <stop offset="1" stop-color="var(--maroon-deep)"/>
        </linearGradient>
        <clipPath id="label-b-clip"><rect width="502" height="1375"/></clipPath>
      </defs>
      <g clip-path="url(#label-b-clip)">
        <rect class="label-paper" width="502" height="1375" fill="var(--paper)"/>

        <g class="brand-lockup">
          <circle cx="251" cy="150" r="50" fill="var(--maroon)"/>
          <text class="brand-name" x="251" y="265" font-size="50" text-anchor="middle">HARBOR HIDE</text>
          <text class="brand-name" x="251" y="289" font-size="17" text-anchor="middle" letter-spacing="1">REVIVAL, INC</text>
        </g>

        <path class="maroon-band" d="M0,380 C150,340 350,330 502,345 L502,1375 L0,1375 Z" fill="var(--maroon)"/>
        <path d="M0,376 C150,336 350,326 502,341" fill="none" stroke="var(--charcoal)" stroke-width="14"/>

        <path class="seat-photo" d="M0,430 C120,392 330,362 470,376 C460,600 300,850 0,1010 Z" fill="url(#seat-black)" role="img" aria-label="Photo of black quilted leather car seats with red piping"/>

        <path class="swoosh" d="M0,1015 C300,875 470,690 502,640 L502,700 C420,875 250,1005 0,1085 Z" fill="var(--paper)"/>
        <path d="M0,1050 C290,930 460,750 502,690" fill="none" stroke="var(--charcoal)" stroke-width="12"/>
        <path d="M0,1080 C250,1000 420,870 502,700 L502,1375 L0,1375 Z" fill="url(#maroon-b)"/>
        <path d="M180,1375 C320,1300 440,1225 502,1180 L502,1375 Z" fill="var(--maroon-bright)"/>

        <g class="product-title" transform="rotate(-16 250 1160)">
          <text class="product-word" x="38" y="1160" font-size="138" textLength="400" lengthAdjust="spacingAndGlyphs" fill="url(#gold-b)">Leather</text>
          <text class="product-line" x="132" y="1206" font-size="50" textLength="272" lengthAdjust="spacingAndGlyphs">CLEANER &amp;</text>
          <text class="product-line" x="112" y="1260" font-size="50" textLength="345" lengthAdjust="spacingAndGlyphs">CONDITIONER</text>
        </g>

        <text class="net-weight" x="370" y="1312" font-size="34" text-anchor="middle" font-style="italic" fill="var(--paper)">16 oz</text>
      </g>
    </svg>
  </section>
</main>
</body>
</html>
```